Boutique Film/TV Company needs Business Card Design

Please see our website for background on our company and look of our current logo: www.lumarocpictures.ca

Pantone 314U is our main colour.

Target Market(s)

Network of peers, funders and broadcasters.

Industry/Entity Type

Business

Requirements
Must have
• We would like rounded corners and the height of the card to be shorter than traditional (maybe?!)

It's important that we have room for our office address, office number, cell number, email address, website, facebook and linked-in info (though not all of us have a linked-in account).

Would like the logo to keep the exclamation marks over the letters but the tag line/tag words of "film - television - interactive" can stay or go or... surprise me!

Nice to have
• Silky matte finish.

We are open to a change in the font of our logo/name.

```html
<!DOCTYPE html>
<html lang="en">
<head>
<meta charset="utf-8">
<title>Lumaroc Business Card</title>
<link rel="stylesheet" href="https://fonts.googleapis.com/css2?family=Open+Sans:wght@400;600;700&display=swap">
<style>
  :root {
    --teal: #0f7390;
    --teal-deep: #0a6583;
    --teal-light: #4ea5b9;
    --paper: #ffffff;
    --ink: #1e1e1e;
    --grey: #6a6a6a;
    --backdrop: #cfcfcf;
  }
  * { margin: 0; padding: 0; box-sizing: border-box; }
  html, body { width: 1200px; height: 900px; overflow: hidden; }
  body {
    background: var(--backdrop);
    font-family: "Open Sans", Arial, sans-serif;
    position: relative;
  }
  .card {
    position: absolute;
    top: 300px;
    width: 500px;
    height: 300px;
    border-radius: 22px;
    overflow: hidden;
    box-shadow: 0 10px 28px rgba(0,0,0,0.22);
  }
  .card--front { left: 60px; background: var(--paper); }
  .card--back {
    left: 640px;
    background: linear-gradient(135deg, var(--teal-deep) 0%, var(--teal) 45%, var(--teal-light) 100%);
    color: var(--paper);
  }
  .tab {
    position: absolute;
    width: 110px;
    height: 16px;
    border-radius: 8px;
  }
  .card--front .tab { background: var(--teal); }
  .card--back .tab { background: var(--paper); }
  .tab--top { top: 14px; right: -20px; }
  .tab--bottom { bottom: 14px; left: -20px; }

  .brand { text-align: center; }
  .brand__name { font-weight: 400; letter-spacing: 1px; line-height: 1; }
  .brand__tagline { font-weight: 600; letter-spacing: 0.3px; }

  .card--front .brand { margin-top: 34px; }
  .card--front .brand__name { font-size: 44px; color: var(--ink); }
  .card--front .brand__tagline { font-size: 11px; color: var(--teal); margin-top: 6px; }

  .person { text-align: center; margin-top: 16px; }
  .person__name { font-size: 24px; font-weight: 700; color: var(--ink); line-height: 1.1; }
  .person__role { font-size: 13px; color: var(--grey); }

  .contact {
    display: flex;
    justify-content: space-between;
    margin: 18px 48px 0;
    font-size: 10.5px;
    color: var(--grey);
    line-height: 1.7;
  }
  .contact__item { display: flex; align-items: center; gap: 6px; }
  .contact__icon { width: 10px; height: 10px; fill: var(--teal); flex: none; }
  .contact__dot { width: 8px; height: 8px; border-radius: 50%; background: var(--teal); flex: none; }

  .card--back .brand { margin-top: 78px; }
  .card--back .brand__name { font-size: 64px; }
  .card--back .brand__tagline { font-size: 15px; margin-top: 10px; }
  .card--back .brand__web { font-size: 13px; margin-top: 8px; letter-spacing: 0.3px; }
</style>
</head>
<body>

<section class="card card--front" aria-label="Business card front">
  <span class="tab tab--top"></span>
  <span class="tab tab--bottom"></span>

  <div class="brand">
    <div class="brand__name">Lumaroc</div>
    <div class="brand__tagline">Films • Television • Interactive</div>
  </div>

  <div class="person">
    <div class="person__name">Name Surname</div>
    <div class="person__role">Position</div>
  </div>

  <div class="contact">
    <ul class="contact__column" style="list-style:none">
      <li class="contact__item">
        <svg class="contact__icon" viewBox="0 0 10 10"><path d="M5 0.5 L10 5 H8.5 V9.5 H6 V6.5 H4 V9.5 H1.5 V5 H0 Z"/></svg>
        #48 Harbour Lane, Easton Falls, PA 19020
      </li>
      <li class="contact__item">
        <svg class="contact__icon" viewBox="0 0 10 10"><path d="M2 0.5 L4 2.8 L3 4 Q4.5 6 6 7 L7.2 6 L9.5 8 L8 9.6 Q3.5 9 0.4 2 Z"/></svg>
        610.555.0142
      </li>
      <li class="contact__item">
        <svg class="contact__icon" viewBox="0 0 10 10"><rect x="2.5" y="0.5" width="5" height="9" rx="1"/></svg>
        237.555.0187
      </li>
      <li class="contact__item">
        <svg class="contact__icon" viewBox="0 0 10 10"><path d="M0.5 2 H9.5 V8 H0.5 Z M0.5 2 L5 5.5 L9.5 2" stroke="#fff" stroke-width="0.8"/></svg>
        name@lumarocpictures.ca
      </li>
    </ul>
    <ul class="contact__column" style="list-style:none">
      <li class="contact__item"><span class="contact__dot"></span>lumaroc.social</li>
      <li class="contact__item"><span class="contact__dot"></span>lumaroc.network</li>
      <li class="contact__item">
        <svg class="contact__icon" viewBox="0 0 10 10"><rect x="0.5" y="1" width="9" height="6" rx="0.8"/><rect x="3.5" y="7.5" width="3" height="1.5"/></svg>
        www.lumarocpictures.ca
      </li>
    </ul>
  </div>
</section>

<section class="card card--back" aria-label="Business card back">
  <span class="tab tab--top"></span>
  <span class="tab tab--bottom"></span>

  <div class="brand">
    <div class="brand__name">Lumaroc</div>
    <div class="brand__tagline">Films • Television • Interactive</div>
    <div class="brand__web">www.lumarocpictures.ca</div>
  </div>
</section>

</body>
</html>
```